Business card design needed

Family General Practitioner/ Family Physician.
Logo is the logo of the Crestmoor Guild of Family Clinicians Australia
http://kvplm.tarevo.edu.au/PictureGallery/logos/pages/CGFC%20logo_jpg.htm

Reason: Just a bit more time to make changes and the weekend for me to look at things closely and to choose. Thanks, Lumi

Thanks for all the submissions. So many of them are really works of art. Not one of them are not good. The ones that I am eliminating are the ones that I think are not suitable for me personally only, and because if I don't, it makes it very difficult to decide as many of you are also sending me slight variations of a card. I have just decided to choose a second place card too. Can't thank you all enough. Good luck, Lumi. P.S - Working today till 10 pm as the card says :-), so probably won't be able to give a feedback till late Saturday night or Sunday morning here in Sydney, Australia. 

Reason: Just added a second place to the budget and realised that Australia is ahead of the rest of the world in the time zone (only :-) - don't want to offend anyone or start a debate!! ) , so Monday deadline will mean it will be a weekend for the rest of the world. Just wanted to give everyone more time to submit their best, especially since I will be picking a second card too. Can't thank everyone enough for the submissions. P.S - Not keen on photos on the card.

Contact Information for Business Card

Dr. Lumi Harcourt M.B.B.S., F.C.G.F.C
Family General Practitioner
Address, timings, phone and fax number on the back.

Requirements
Must have
• Timings
Mon 7 am - 7 pm
Tues 7 am - 12 pm
Wed 7 am - 10 pm
Thurs 7 am - 12 pm
Fri 7 am - 8 pm
Sat 8 am - 10 pm
Sun - Off

```html
<!DOCTYPE html>
<html lang="en">
<head>
<meta charset="utf-8">
<title>Dr. Lumi Harcourt – Business Card</title>
<link href="https://fonts.googleapis.com/css2?family=Nunito:wght@300;400;600&display=swap" rel="stylesheet">
<style>
  :root {
    --page-bg: #ecebe8;
    --card-light: #f4f8fb;
    --card-mid: #d6e6f0;
    --card-blue: #7fb8d4;
    --card-deep: #4e9dc4;
    --text-blue: #5aa6cf;
    --text-grey: #7d8a94;
    --text-dark: #3f4b55;
    --accent-orange: #e8a21a;
    --emblem-tone: #e6ddc8;
  }
  * { box-sizing: border-box; margin: 0; padding: 0; }
  html, body { width: 1200px; height: 801px; overflow: hidden; }
  body {
    background: var(--page-bg);
    font-family: "Nunito", Arial, sans-serif;
    display: flex;
    align-items: center;
    justify-content: center;
    gap: 50px;
  }
  .card {
    position: relative;
    width: 540px;
    height: 309px;
    border-radius: 4px;
    overflow: hidden;
    box-shadow: 0 6px 18px rgba(0,0,0,.18);
  }
  .card::after {
    content: "";
    position: absolute;
    inset: 0;
    background: repeating-linear-gradient(135deg, rgba(255,255,255,.18) 0 1px, transparent 1px 4px);
    pointer-events: none;
  }

  /* Back: hours, emblem, address */
  .card-back {
    background: linear-gradient(180deg, var(--card-light) 0%, var(--card-mid) 100%);
  }
  .card-back .side-band {
    position: absolute;
    right: 0; top: 0;
    width: 120px; height: 100%;
    background: linear-gradient(180deg, var(--card-blue), var(--card-deep));
    clip-path: polygon(30% 0, 100% 0, 100% 100%, 0 100%);
  }
  .emblem {
    position: absolute;
    left: 24px; top: 58px;
    width: 150px; height: 150px;
    display: flex; flex-direction: column;
    align-items: center; justify-content: center;
    gap: 10px;
  }
  .emblem-mark {
    width: 90px; height: 90px;
    border-radius: 50%;
    background: radial-gradient(circle, #f3eee2, var(--emblem-tone));
  }
  .emblem-name {
    font-weight: 600;
    font-size: 22px;
    letter-spacing: 2px;
    color: var(--text-dark);
  }
  .hours {
    position: absolute;
    left: 190px; top: 18px;
    color: var(--text-blue);
  }
  .hours-title {
    font-weight: 300;
    font-size: 24px;
    line-height: 1.3;
    margin-bottom: 4px;
  }
  .hours-table {
    border-collapse: collapse;
    font-weight: 300;
    font-size: 15px;
    line-height: 1.3;
    color: var(--text-grey);
  }
  .hours-table td { padding: 1px 0; }
  .hours-table td.day { width: 110px; color: var(--text-blue); }
  .address {
    position: absolute;
    left: 28px; bottom: 14px;
    display: flex; gap: 10px; align-items: flex-start;
    font-size: 11px;
    line-height: 1.4;
    color: var(--text-dark);
  }
  .address svg { flex: none; margin-top: 2px; }

  /* Front: name and title */
  .card-front {
    background: linear-gradient(200deg, #f6f9fb 0%, #dce9f1 55%, #b9d4e4 100%);
  }
  .front-name {
    position: absolute;
    left: 40px; top: 70px;
    font-weight: 300;
    font-size: 46px;
    color: #ffffff;
    text-shadow: 0 1px 2px rgba(70,120,150,.35);
    letter-spacing: 1px;
  }
  .front-quals {
    position: absolute;
    left: 44px; top: 134px;
    font-weight: 400;
    font-size: 17px;
    letter-spacing: 3px;
    color: #ffffff;
    text-shadow: 0 1px 2px rgba(70,120,150,.35);
  }
  .front-role {
    position: absolute;
    left: 44px; bottom: 40px;
    font-weight: 400;
    font-size: 20px;
    color: var(--text-dark);
  }
</style>
</head>
<body>
  <section class="card card-back">
    <div class="side-band"></div>
    <div class="emblem" role="img" aria-label="Crestmoor Guild of Family Clinicians Australia emblem">
      <div class="emblem-mark"></div>
      <span class="emblem-name">CGFC</span>
    </div>
    <div class="hours">
      <h2 class="hours-title">Working Hours</h2>
      <table class="hours-table">
        <tr><td class="day">Monday</td><td>7am - 7pm</td></tr>
        <tr><td class="day">Tuesday</td><td>7am - 12pm</td></tr>
        <tr><td class="day">Wednesday</td><td>7am - 10pm</td></tr>
        <tr><td class="day">Thursday</td><td>7am - 12pm</td></tr>
        <tr><td class="day">Friday</td><td>7am - 8pm</td></tr>
        <tr><td class="day">Saturday</td><td>8am - 10pm</td></tr>
        <tr><td class="day">Sunday</td><td>Off</td></tr>
      </table>
    </div>
    <div class="address">
      <svg width="14" height="18" viewBox="0 0 14 18" aria-hidden="true">
        <path d="M7 0C3.1 0 0 3.1 0 7c0 5 7 11 7 11s7-6 7-11c0-3.9-3.1-7-7-7z" fill="var(--accent-orange)"/>
        <circle cx="7" cy="7" r="2.6" fill="#fff"/>
      </svg>
      <p>Upper Level, Arbor Court, Linden Vale Shopping Centre<br>
         Linden Vale, NSW 2199<br>
         P: 02 5550 2400 &nbsp; F: 02 5550 2255</p>
    </div>
  </section>

  <section class="card card-front">
    <h1 class="front-name">Dr. Lumi Harcourt</h1>
    <p class="front-quals">MBBS FCGFC</p>
    <p class="front-role">Family General Practitioner</p>
  </section>
</body>
</html>
```